PowerPoint Template for our Business

We are looking for a professional and visually appealing PowerPoint template for our business, Pellion Labs. We specialize in calibration services and are currently undergoing a rebranding process. The new template should align with our updated brand identity, using the provided color palette and logos.
Project Requirements:
Title Slide:
Full Pellion Labs logo prominently displayed.
Clean and professional layout.
Background color should be white with brand accents.
Title and subtitle areas clearly defined.
Content Slide:
Consistent use of brand colors for headers, footers, and other elements.
Space for text, images, charts, and graphs.
PX logo subtly incorporated.
Clean and modern layout ensuring readability and professionalism.
Section Header Slide:
Clear differentiation from content slides.
Use of PX logo and brand color for background.
Professional typography.
Closing Slide:
Full Pellion Labs logo with a final message.
Clean background, professional layout.
Space for a thank you message and contact information.
Brand Colors:
Green: RGB (207, 255, 0)
Light Gray: RGB (239, 239, 239)
Gray: RGB (191, 191, 191)
Black: RGB (0, 0, 0)
White: RGB (255, 255, 255)
Deliverables:
A fully editable PowerPoint template (.pptx format).
Fonts and any additional assets used in the design.
Additional Information:
Please refer to the attached logos and color palette for guidance.
We are looking for a design that is not only professional and visually appealing but also functional for business presentations.
We look forward to seeing your creative proposals and selecting a design that best represents our brand.
Thank you!

```html
<!DOCTYPE html>
<html lang="en">
<head>
<meta charset="utf-8">
<title>Pellion Labs – Presentation Template Overview</title>
<link rel="stylesheet" href="https://fonts.googleapis.com/css2?family=Archivo:wght@400;500;600;700;800&display=swap">
<style>
  :root{
    --green:#cfff00;
    --light:#efefef;
    --gray:#bfbfbf;
    --dark-gray:#7f7f7f;
    --black:#000;
    --white:#fff;
    --muted:#8a8a8a;
  }
  html,body{margin:0;padding:0;background:var(--black);overflow:hidden}
  .board{position:relative;width:969px;height:1200px;background:var(--black);font-family:"Archivo",sans-serif;overflow:hidden}
  .slide{position:absolute;width:380px;height:219px;background:var(--white);overflow:hidden;transform:scale(.558);transform-origin:0 0;color:var(--black)}
  .slide > *{position:absolute;margin:0;box-sizing:border-box}
  .slide svg{font-family:"Archivo",sans-serif}
  .chart{left:0;top:0;width:380px;height:219px}
  .title{left:26px;top:15px;font-size:17px;font-weight:600;line-height:20px}
  .rule{left:24px;right:44px;top:42px;height:1px;background:var(--black)}
  .tab{right:0;top:11px;width:54px;height:31px;background:var(--black);clip-path:polygon(24% 0,100% 0,100% 100%,0 100%);color:var(--green);font-weight:800;font-size:14px;line-height:31px;text-align:center;padding-left:10px}
  .date{left:26px;bottom:9px;font-size:4px;color:var(--muted)}
  .page{right:20px;bottom:0;width:18px;height:19px;background:var(--green);font-size:5px;font-weight:700;text-align:center;line-height:19px}
  .body{font-size:9.5px;line-height:1.12;color:var(--black)}
  .body ul{margin:0;padding-left:10px}
  .body li{margin-bottom:10px}
  .photo{background:linear-gradient(135deg,#5a5f66,#2c2f33 60%,#8a7a5c)}
  .photo.warm{background:linear-gradient(135deg,#6b6a66,#a9a39a 45%,#d8782e 70%,#3a3c40)}
  .photo.city{background:linear-gradient(120deg,#1d2430,#6a5a3c 40%,#e0b060 55%,#26303e)}
  .photo.lab{background:linear-gradient(120deg,#dfe6ea,#7fa0b4 40%,#1e3a3e 60%,#cfd8dc)}
  .photo.dark{background:radial-gradient(circle at 50% 45%,#e8e8e8 0 8%,#2a2a2a 20%,#0c0c0c 80%)}
  .brand-mark{width:40px;height:36px;background:var(--black)}
  .brand-name{font-weight:500;color:var(--black)}
  .black-card{background:var(--black);color:var(--white)}
</style>
</head>
<body>
<main class="board">

<!-- Row 1 -->
<section class="slide" style="left:38.5px;top:38.5px">
  <div class="brand-mark" style="left:19px;top:27px"></div>
  <div class="brand-name" style="left:70px;top:34px;font-size:20px">Pellion Labs</div>
  <div style="left:19px;top:67px;width:342px;height:100px;background:var(--green)"></div>
  <h1 style="left:36px;top:92px;font-size:18px;font-weight:700;line-height:19px">Replace Text With<br>Slide Title</h1>
  <div style="left:19px;top:160px;width:222px;height:21px;background:var(--black);color:var(--white);font-size:8px;line-height:21px;padding-left:20px">Subtitle Comes Here</div>
</section>

<section class="slide" style="left:266.7px;top:38.5px">
  <div style="left:12px;top:49px;width:368px;height:119px;background:var(--black)"></div>
  <div style="left:260px;top:0;width:107px;height:199px;background:var(--green)"></div>
  <div class="brand-mark" style="left:14px;top:20px;width:30px;height:28px"></div>
  <div class="brand-name" style="left:56px;top:24px;font-size:16px">Pellion Labs</div>
  <h1 style="left:35px;top:93px;font-size:18px;font-weight:700;line-height:19px;color:var(--white)">Replace Text With<br>Slide Title</h1>
  <div style="left:32px;top:161px;width:190px;height:21px;background:var(--gray);font-size:8px;line-height:21px;padding-left:6px">Subtitle Comes Here</div>
  <div style="left:275px;top:185px;font-size:7px;font-weight:700">Date:</div>
</section>

<section class="slide" style="left:496.1px;top:38.5px">
  <h2 class="title">Table of Contents</h2><i class="rule"></i><div class="tab">PX</div>
  <svg class="chart" viewBox="0 0 380 219">
    <g fill="#000"><rect x="0" y="44" width="380" height="44"/><rect x="0" y="96" width="380" height="44"/><rect x="0" y="149" width="380" height="44"/></g>
    <g fill="#cfff00" font-size="15" font-weight="700">
      <text x="30" y="72">01.</text><text x="208" y="72">04.</text>
      <text x="30" y="124">02.</text><text x="208" y="124">05.</text>
      <text x="30" y="177">03.</text><text x="208" y="177">06.</text>
    </g>
    <g fill="#fff" font-size="6" font-weight="700">
      <text x="62" y="63">About us</text><text x="240" y="63">Team</text>
      <text x="62" y="115">Portfolio</text><text x="240" y="115">Future</text>
      <text x="62" y="168">Our Services</text><text x="240" y="168">What Next?</text>
    </g>
    <g fill="#9a9a9a" font-size="3.6">
      <text x="62" y="71">Short line of text about this part</text><text x="62" y="76">of the deck.</text>
      <text x="240" y="71">Short line of text about this part</text><text x="240" y="76">of the deck.</text>
      <text x="62" y="123">Short line of text about this part</text><text x="62" y="128">of the deck.</text>
      <text x="240" y="123">Short line of text about this part</text><text x="240" y="128">of the deck.</text>
      <text x="62" y="176">Short line of text about this part</text><text x="62" y="181">of the deck.</text>
      <text x="240" y="176">Short line of text about this part</text><text x="240" y="181">of the deck.</text>
    </g>
  </svg>
  <span class="date">05/14/2024</span><span class="page">3</span>
</section>

<section class="slide" style="left:724.3px;top:38.5px">
  <div class="photo warm" role="img" aria-label="Technician in hard hat and safety vest calibrating equipment" style="left:0;top:0;width:144px;height:219px"></div>
  <div class="black-card" style="left:120px;top:63px;width:240px;height:101px"></div>
  <div style="left:167px;top:78px;font-size:15px;font-weight:700;color:var(--green)">01</div>
  <h2 style="left:166px;top:101px;font-size:23px;font-weight:700;line-height:25px;color:var(--white)">Name of<br>the section</h2>
</section>

<!-- Row 2 -->
<section class="slide" style="left:38.5px;top:178.6px">
  <h2 class="title">Plan</h2><i class="rule"></i><div class="tab">PX</div>
  <svg class="chart" viewBox="0 0 380 219">
    <rect x="22" y="51" width="340" height="22" fill="#000"/>
    <g fill="#fff" font-size="6"><text x="26" y="65">Key partners</text><text x="86" y="65">Key activities</text><text x="154" y="65">Value propositions</text><text x="238" y="61">Customer</text><text x="238" y="68">relationships</text><text x="306" y="61">Customer</text><text x="306" y="68">segments</text></g>
    <g fill="none" stroke="#000" stroke-width=".6"><rect x="22" y="73" width="340" height="75"/><line x1="83" y1="73" x2="83" y2="148"/><line x1="150" y1="73" x2="150" y2="148"/><line x1="235" y1="73" x2="235" y2="148"/><line x1="303" y1="73" x2="303" y2="148"/><rect x="22" y="165" width="340" height="30"/><line x1="192" y1="165" x2="192" y2="195"/></g>
    <rect x="83" y="105" width="67" height="12" fill="#cfff00"/><rect x="235" y="105" width="68" height="12" fill="#cfff00"/>
    <g font-size="5.5"><text x="86" y="113">Key resources</text><text x="238" y="113">Channels</text></g>
    <rect x="22" y="148" width="340" height="17" fill="#000"/>
    <g fill="#fff" font-size="6"><text x="26" y="159">Cost structure</text><text x="196" y="159">Revenue streams</text></g>
    <g fill="#777" font-size="3.5">
      <text x="25" y="80">Name the partners</text><text x="25" y="85">your work relies on</text>
      <text x="86" y="80">List the tasks that</text><text x="86" y="85">create value</text>
      <text x="153" y="80">Show what sets you</text><text x="153" y="85">apart from others</text>
      <text x="238" y="80">How you keep in</text><text x="238" y="85">touch with clients</text>
      <text x="306" y="80">Name the client</text><text x="306" y="85">groups you serve</text>
      <text x="86" y="123">Note the resources</text><text x="86" y="128">your plan needs</text>
      <text x="238" y="123">How you reach and</text><text x="238" y="128">engage clients</text>
      <text x="25" y="172">Note fixed and variable costs tied to the business</text>
      <text x="195" y="172">Note the sources of revenue for the business</text>
    </g>
  </svg>
  <span class="date">05/14/2024</span><span class="page">5</span>
</section>

<section class="slide" style="left:266.7px;top:178.6px">
  <h2 class="title">What We do</h2><i class="rule"></i><div class="tab">PX</div>
  <svg class="chart" viewBox="0 0 380 219">
    <rect x="18" y="57" width="109" height="123" fill="#000"/><rect x="141" y="57" width="109" height="123" fill="#bfbfbf"/><rect x="263" y="57" width="109" height="123" fill="#000"/>
    <g fill="#fff" font-size="13" font-weight="700"><text x="28" y="85">01.</text><text x="151" y="85">02.</text><text x="273" y="85">03.</text></g>
    <g fill="#cfff00" font-size="5.5" font-weight="700"><text x="28" y="98">Lorem Ipsum</text><text x="151" y="98" fill="#fff">Lorem Ipsum</text><text x="273" y="98">Lorem Ipsum</text></g>
    <line x1="28" y1="104" x2="117" y2="104" stroke="#555" stroke-width=".5"/><line x1="151" y1="104" x2="240" y2="104" stroke="#fff" stroke-width=".5"/><line x1="273" y1="104" x2="362" y2="104" stroke="#555" stroke-width=".5"/>
    <g fill="#fff" font-size="4.5"><text x="28" y="115">Short line of body text here,</text><text x="28" y="121">set in two rows</text><text x="151" y="115">Short line of body text here,</text><text x="151" y="121">set in two rows</text><text x="273" y="115">Short line of body text here,</text><text x="273" y="121">set in two rows</text></g>
    <g fill="#cfff00"><path d="M105 84l8-8 2 2-8 8-3 1z"/><circle cx="232" cy="80" r="4"/><circle cx="355" cy="79" r="3"/><rect x="354" y="83" width="2" height="4"/><rect x="28" y="176" width="10" height="4"/><rect x="151" y="176" width="10" height="4"/><rect x="273" y="176" width="10" height="4"/></g>
  </svg>
  <span class="date">05/14/2024</span><span class="page">6</span>
</section>

<section class="slide" style="left:496.1px;top:178.6px">
  <h2 class="title">Our Values</h2><i class="rule"></i><div class="tab">PX</div>
  <svg class="chart" viewBox="0 0 380 219">
    <rect x="0" y="75" width="380" height="55" fill="#000"/>
    <g fill="#bfbfbf" stroke="#efefef" stroke-width="4"><circle cx="60" cy="72" r="21"/><circle cx="146" cy="72" r="21"/><circle cx="233" cy="72" r="21"/><circle cx="319" cy="72" r="21"/></g>
    <g fill="none" stroke="#fff" stroke-width="1.4"><rect x="52" y="64" width="16" height="12"/><line x1="60" y1="76" x2="60" y2="82"/><circle cx="146" cy="72" r="4"/><circle cx="138" cy="65" r="2"/><circle cx="154" cy="65" r="2"/><circle cx="138" cy="79" r="2"/><circle cx="154" cy="79" r="2"/><rect x="226" y="63" width="11" height="15"/><circle cx="239" cy="77" r="3"/><rect x="312" y="64" width="13" height="15"/><line x1="314" y1="78" x2="325" y2="66"/></g>
    <g fill="#fff" font-size="7" font-weight="700" text-anchor="middle"><text x="60" y="113">Lorem Ipsum</text><text x="146" y="113">Lorem Ipsum</text><text x="233" y="113">Lorem Ipsum</text><text x="319" y="113">Lorem Ipsum</text></g>
    <g fill="#efefef"><rect x="21" y="130" width="78" height="67"/><rect x="108" y="130" width="78" height="67"/><rect x="194" y="130" width="78" height="67"/><rect x="281" y="130" width="78" height="67"/></g>
    <g fill="#555" font-size="4.5" text-anchor="middle">
      <text x="60" y="143">Short note on this value</text><text x="60" y="149">that the team holds,</text><text x="60" y="155">kept brief and clear.</text>
      <text x="146" y="143">Short note on this value</text><text x="146" y="149">that the team holds,</text><text x="146" y="155">kept brief and clear.</text>
      <text x="233" y="143">Short note on this value</text><text x="233" y="149">that the team holds,</text><text x="233" y="155">kept brief and clear.</text>
      <text x="319" y="143">Short note on this value</text><text x="319" y="149">that the team holds,</text><text x="319" y="155">kept brief and clear.</text>
    </g>
  </svg>
  <span class="date">05/14/2024</span><span class="page">7</span>
</section>

<section class="slide" style="left:724.3px;top:178.6px">
  <h2 class="title">Our Process</h2><i class="rule"></i><div class="tab">PX</div>
  <svg class="chart" viewBox="0 0 380 219">
    <g fill="none" stroke="#000" stroke-width="1.2"><rect x="42" y="58" width="12" height="10"/><circle cx="40" cy="72" r="3"/><rect x="124" y="58" width="14" height="16"/><line x1="127" y1="64" x2="135" y2="64"/><path d="M218 58l3 6 6 1-4 4 1 6-6-3-6 3 1-6-4-4 6-1z"/><circle cx="306" cy="65" r="8"/><path d="M302 73l-2 7 6-3 6 3-2-7"/></g>
    <rect x="12" y="88" width="355" height="37" fill="#000"/>
    <g fill="#cfff00"><circle cx="50" cy="88" r="3"/><circle cx="136" cy="88" r="3"/><circle cx="222" cy="88" r="3"/><circle cx="308" cy="88" r="3"/></g>
    <g fill="#fff" font-size="5.5" font-weight="700"><text x="32" y="109">Lorem Ipsum</text><text x="118" y="109">Lorem Ipsum</text><text x="204" y="109">Lorem Ipsum</text><text x="290" y="109">Lorem Ipsum</text></g>
    <g fill="#fff"><circle cx="94" cy="107" r="5"/><circle cx="180" cy="107" r="5"/><circle cx="266" cy="107" r="5"/><circle cx="352" cy="107" r="5"/></g>
    <g fill="none" stroke="#000" stroke-width="1.2"><path d="M91 107h6m-2-2l2 2-2 2"/><path d="M177 107h6m-2-2l2 2-2 2"/><path d="M263 107h6m-2-2l2 2-2 2"/><path d="M349 107h6m-2-2l2 2-2 2"/></g>
    <rect x="12" y="125" width="355" height="70" fill="#efefef"/>
    <g fill="#555" font-size="4.5">
      <text x="22" y="140">Short note on this step,</text><text x="22" y="146">what happens and</text><text x="22" y="152">who takes part in it</text><text x="22" y="158">before moving on.</text>
      <text x="108" y="140">Short note on this step,</text><text x="108" y="146">what happens and</text><text x="108" y="152">who takes part in it</text><text x="108" y="158">before moving on.</text>
      <text x="194" y="140">Short note on this step,</text><text x="194" y="146">what happens and</text><text x="194" y="152">who takes part in it</text><text x="194" y="158">before moving on.</text>
      <text x="280" y="140">Short note on this step,</text><text x="280" y="146">what happens and</text><text x="280" y="152">who takes part in it</text><text x="280" y="158">before moving on.</text>
    </g>
  </svg>
  <span class="date">05/14/2024</span><span class="page">8</span>
</section>

<!-- Row 3 -->
<section class="slide" style="left:38.5px;top:318.1px">
  <h2 class="title">How we do it</h2><i class="rule"></i><div class="tab">PX</div>
  <svg class="chart" viewBox="0 0 380 219">
    <g fill="none" stroke-width="20">
      <path d="M189 68A52 52 0 0 1 241 120" stroke="#cfff00"/>
      <path d="M241 120A52 52 0 0 1 189 172" stroke="#000"/>
      <path d="M189 172A52 52 0 0 1 137 120" stroke="#7f7f7f"/>
      <path d="M137 120A52 52 0 0 1 189 68" stroke="#bfbfbf"/>
    </g>
    <circle cx="189" cy="120" r="38" fill="#efefef"/>
    <g fill="none" stroke="#999" stroke-width="1"><rect x="182" y="110" width="12" height="16"/><circle cx="196" cy="126" r="5"/></g>
    <g fill="#fff" stroke="#777" stroke-width=".8"><circle cx="153" cy="84" r="6"/><circle cx="225" cy="84" r="6"/><circle cx="153" cy="156" r="6"/><circle cx="225" cy="156" r="6"/></g>
    <g fill="none" stroke="#000" stroke-width="1"><path d="M150 84l2 2 4-4"/><path d="M222 84l2 2 4-4"/><path d="M150 156l2 2 4-4"/><path d="M222 156l2 2 4-4"/></g>
    <g fill="#333" font-size="5.5" text-anchor="middle">
      <text x="80" y="60">Short line of text for</text><text x="80" y="67">this point, with a</text><text x="80" y="74">little more detail to</text><text x="80" y="81">round it off nicely</text><text x="80" y="88">in a few rows</text>
      <text x="80" y="143">Short line of text for</text><text x="80" y="150">this point, with a</text><text x="80" y="157">little more detail to</text><text x="80" y="164">round it off nicely</text><text x="80" y="171">in a few rows</text>
    </g>
    <g fill="#333" font-size="5.5">
      <text x="272" y="60">Short line of text for</text><text x="272" y="67">this point, with a</text><text x="272" y="74">little more detail to</text><text x="272" y="81">round it off nicely</text><text x="272" y="88">in a few rows</text>
      <text x="272" y="143">Short line of text for</text><text x="272" y="150">this point, with a</text><text x="272" y="157">little more detail to</text><text x="272" y="164">round it off nicely</text><text x="272" y="171">in a few rows</text>
    </g>
    <g fill="#000"><circle cx="124" cy="58" r="1"/><circle cx="265" cy="58" r="1"/><circle cx="124" cy="141" r="1"/><circle cx="265" cy="141" r="1"/></g>
  </svg>
  <span class="page">9</span>
</section>

<section class="slide" style="left:266.7px;top:318.1px">
  <h2 class="title">Market Segmentation</h2><i class="rule"></i><div class="tab">PX</div>
  <svg class="chart" viewBox="0 0 380 219">
    <circle cx="187" cy="126" r="76" fill="#e6e6e6"/>
    <circle cx="187" cy="139" r="62" fill="#000"/>
    <circle cx="187" cy="153" r="48" fill="#cfff00"/>
    <g font-size="7" font-weight="700" text-anchor="middle"><text x="187" y="70">$100M</text><text x="187" y="99" fill="#fff">$20M</text><text x="187" y="153">$5M</text></g>
  </svg>
  <span class="date">05/14/2024</span><span class="page">10</span>
</section>

<section class="slide" style="left:496.1px;top:318.1px">
  <h2 class="title">Slide Title</h2><i class="rule"></i><div class="tab">PX</div>
  <svg class="chart" viewBox="0 0 380 219">
    <g stroke="#e4e4e4" stroke-width=".5"><line x1="34" y1="55" x2="34" y2="175"/><line x1="70" y1="55" x2="70" y2="175"/><line x1="106" y1="55" x2="106" y2="175"/><line x1="142" y1="55" x2="142" y2="175"/><line x1="178" y1="55" x2="178" y2="175"/><line x1="214" y1="55" x2="214" y2="175"/></g>
    <rect x="34" y="62" width="28" height="11" fill="#000"/><rect x="62" y="62" width="50" height="11" fill="#bfbfbf"/><rect x="112" y="62" width="91" height="11" fill="#cfff00"/>
    <rect x="34" y="93" width="64" height="11" fill="#000"/><rect x="98" y="93" width="32" height="11" fill="#bfbfbf"/><rect x="130" y="93" width="54" height="11" fill="#cfff00"/>
    <rect x="34" y="124" width="25" height="11" fill="#000"/><rect x="59" y="124" width="101" height="11" fill="#bfbfbf"/><rect x="160" y="124" width="35" height="11" fill="#cfff00"/>
    <rect x="34" y="155" width="75" height="11" fill="#000"/><rect x="109" y="155" width="29" height="11" fill="#bfbfbf"/><rect x="138" y="155" width="57" height="11" fill="#cfff00"/>
    <g fill="#888" font-size="3.5" text-anchor="end"><text x="31" y="69">Sit</text><text x="31" y="100">Dolor</text><text x="31" y="131">Ipsum</text><text x="31" y="162">Lorem</text></g>
    <g fill="#888" font-size="3.5" text-anchor="middle"><text x="34" y="182">0</text><text x="52" y="182">1000</text><text x="70" y="182">2000</text><text x="88" y="182">3000</text><text x="106" y="182">4000</text><text x="124" y="182">5000</text><text x="142" y="182">6000</text><text x="160" y="182">7000</text><text x="178" y="182">8000</text><text x="196" y="182">9000</text><text x="214" y="182">10000</text><text x="124" y="190">■ Series 1   ■ Series 2   ■ Series 3</text></g>
    <g fill="#333" font-size="5.5"><text x="246" y="81">Short paragraph of body text that</text><text x="246" y="87">sits beside the chart and explains</text><text x="246" y="93">what the bars show across each</text><text x="246" y="99">group in clear and simple words.</text><text x="246" y="105">Keep it to a handful of lines so</text><text x="246" y="111">the reader can scan it quickly</text><text x="246" y="117">and move on to the next point.</text><text x="246" y="123">Add a final note here about the</text><text x="246" y="129">trend and what comes next, with</text><text x="246" y="135">one more line to close the idea</text><text x="246" y="141">and round off the paragraph.</text></g>
  </svg>
  <span class="date">05/14/2024</span><span class="page">11</span>
</section>

<section class="slide" style="left:724.3px;top:318.1px">
  <h2 class="title">Slide Title</h2><i class="rule"></i><div class="tab">PX</div>
  <div class="body" style="left:22px;top:58px;width:190px"><ul><li>Short bullet of body text that runs over a few lines to show how a longer point sits here.</li><li>A second bullet with a little more detail, spread over several lines so the column is filled and the reader gets the full idea.</li></ul></div>
  <div class="photo lab" role="img" aria-label="Lab technician working with samples in front of a data screen" style="left:215px;top:60px;width:152px;height:112px"></div>
  <span class="date">05/14/2024</span><span class="page">12</span>
</section>

<!-- Row 4 -->
<section class="slide" style="left:38.5px;top:458.1px">
  <div class="photo warm" role="img" aria-label="Worker in a yellow safety vest holding a hard hat in a warehouse" style="left:0;top:0;width:380px;height:219px"></div>
  <div class="black-card" style="left:27px;top:164px;width:327px;height:30px;font-size:15px;font-weight:600;text-align:center;line-height:30px">Picture Title. Maybe?</div>
</section>

<section class="slide" style="left:266.7px;top:458.1px">
  <h2 class="title">Slide Title</h2><i class="rule"></i><div class="tab">PX</div>
  <div class="body" style="left:22px;top:58px;width:150px;font-size:9px"><ul><li>Short bullet of body text that runs over a few lines here to fill the space.</li><li>A second bullet with a little more detail, set over several short lines.</li></ul></div>
  <div class="photo city" role="img" aria-label="City traffic lights at night in motion" style="left:177px;top:58px;width:182px;height:62px"></div>
  <div class="photo" role="img" aria-label="Family looking at a tablet together" style="left:177px;top:121px;width:91px;height:59px"></div>
  <div class="photo dark" role="img" aria-label="One bright bulb among dark bulbs" style="left:269px;top:121px;width:90px;height:59px"></div>
  <span class="date">05/14/2024</span><span class="page">14</span>
</section>

<section class="slide" style="left:496.1px;top:458.1px">
  <div class="tab">PX</div>
  <div class="black-card" style="left:22px;top:40px;width:129px;height:142px"></div>
  <div style="left:28px;top:58px;font-size:12px;font-weight:600;color:var(--white)">Slide Title</div>
  <div class="photo dark" role="img" aria-label="One bright bulb among dark bulbs" style="left:22px;top:100px;width:129px;height:82px"></div>
  <div class="body" style="left:156px;top:46px;width:196px;font-size:8px;line-height:1.1"><ul><li style="margin:0">Short bullet of body text that runs over a few lines to fill the space next to the box here.</li><li style="margin:0">A second bullet with a little more text, set over two lines.</li><li style="margin:0"></li></ul></div>
  <div class="photo city" role="img" aria-label="City traffic lights at night in motion" style="left:156px;top:122px;width:210px;height:60px"></div>
  <span class="date">05/14/2024</span>
</section>

<section class="slide" style="left:724.3px;top:458.1px">
  <h2 class="title">Team</h2><i class="rule"></i><div class="tab">PX</div>
  <svg class="chart" viewBox="0 0 380 219">
    <g fill="#efefef"><rect x="20" y="60" width="76" height="127"/><rect x="108" y="60" width="76" height="127"/><rect x="197" y="60" width="76" height="127"/><rect x="285" y="60" width="76" height="127"/></g>
    <g font-size="6.5" font-weight="700" text-anchor="middle"><text x="58" y="130">Lorem Ipsum</text><text x="146" y="130">Lorem Ipsum</text><text x="235" y="130">Lorem Ipsum</text><text x="323" y="130">Lorem Ipsum</text></g>
  </svg>
  <div role="img" aria-label="Portrait of team member" style="left:34px;top:60px;width:48px;height:48px;border-radius:50%;background:radial-gradient(circle,#e6e6e6,#bdbdbd)"></div>
  <div role="img" aria-label="Portrait of team member" style="left:122px;top:60px;width:48px;height:48px;border-radius:50%;background:radial-gradient(circle,#555,#1a1a1a)"></div>
  <div role="img" aria-label="Portrait of team member" style="left:211px;top:60px;width:48px;height:48px;border-radius:50%;background:radial-gradient(circle,#999,#333)"></div>
  <div role="img" aria-label="Portrait of team member" style="left:299px;top:60px;width:48px;height:48px;border-radius:50%;background:radial-gradient(circle,#666,#111)"></div>
  <span class="date">05/14/2024</span><span class="page">16</span>
</section>

<!-- Row 5 -->
<section class="slide" style="left:38.5px;top:597.6px;background:var(--black)">
  <svg class="chart" viewBox="0 0 380 219">
    <g stroke="#fff" stroke-width=".7" fill="none">
      <path d="M200 51v15M116 66h168M116 66v14M284 66v14"/>
      <path d="M116 96v15M85 111h65M85 111v14M150 111v14"/>
      <path d="M284 96v15M252 111h65M252 111v14M317 111v14"/>
      <path d="M85 140v15M55 155h59M55 155v14M114 155v14"/>
      <path d="M317 140v15M229 155h119M229 155v14M289 155v14M348 155v14"/>
    </g>
    <g fill="#fff"><rect x="141" y="36" width="118" height="15"/><rect x="57" y="80" width="119" height="16"/><rect x="224" y="80" width="119" height="16"/><rect x="57" y="125" width="56" height="15"/><rect x="122" y="125" width="55" height="15"/><rect x="224" y="125" width="56" height="15"/><rect x="289" y="125" width="55" height="15"/><rect x="27" y="169" width="56" height="15"/><rect x="87" y="169" width="53" height="15"/><rect x="201" y="169" width="56" height="15"/><rect x="261" y="169" width="56" height="15"/><rect x="320" y="169" width="56" height="15"/></g>
    <g font-size="4" font-weight="700" text-anchor="middle"><text x="200" y="45">CEO</text><text x="116" y="90">CTO</text><text x="284" y="90">CFO</text><text x="85" y="134">Director of IT</text><text x="150" y="134">Director of HR</text><text x="252" y="134">Controller</text><text x="317" y="134">Treasurer</text><text x="55" y="176">Systems</text><text x="55" y="181">administrator</text><text x="114" y="178">IT manager</text><text x="229" y="178">Accounting manager</text><text x="289" y="178">Financial analyst</text><text x="348" y="178">Accounts payable</text></g>
  </svg>
</section>

<section class="slide" style="left:266.7px;top:597.6px">
  <h2 class="title">Road Map I</h2><i class="rule"></i><div class="tab">PX</div>
  <svg class="chart" viewBox="0 0 380 219">
    <g fill="#f4f4f4"><rect x="50" y="64" width="316" height="22"/><rect x="50" y="100" width="316" height="22"/><rect x="50" y="136" width="316" height="22"/><rect x="50" y="173" width="316" height="22"/></g>
    <g stroke="#ddd" stroke-width=".5"><line x1="110" y1="56" x2="110" y2="196"/><line x1="160" y1="56" x2="160" y2="196"/><line x1="211" y1="56" x2="211" y2="196"/><line x1="261" y1="56" x2="261" y2="196"/><line x1="312" y1="56" x2="312" y2="196"/></g>
    <g fill="#888" font-size="4"><text x="62" y="53">◆ Phase 01</text><text x="112" y="53">◆ Phase 01</text><text x="162" y="53">◆ Phase 03</text><text x="213" y="53">◆ Phase 04</text><text x="263" y="53">◆ Phase 05</text><text x="314" y="53">◆ Phase 06</text></g>
    <circle cx="30" cy="73" r="13" fill="#000"/><circle cx="30" cy="111" r="13" fill="#fff" stroke="#000" stroke-width=".8"/><circle cx="30" cy="147" r="13" fill="#000"/><circle cx="30" cy="184" r="13" fill="#fff" stroke="#000" stroke-width=".8"/>
    <g fill="#fff"><rect x="26" y="69" width="8" height="8" rx="1"/><rect x="26" y="146" width="2" height="5"/><rect x="29" y="143" width="2" height="8"/><rect x="32" y="145" width="2" height="6"/></g>
    <g fill="#000"><path d="M26 109h8l-1 6h-6z"/><rect x="26" y="180" width="6" height="6"/><rect x="28" y="182" width="6" height="6" fill="#777"/></g>
    <g fill="#000"><rect x="60" y="69" width="48" height="12" rx="2"/><rect x="111" y="69" width="47" height="12" rx="2"/><rect x="161" y="69" width="101" height="12" rx="2"/><rect x="312" y="69" width="50" height="12" rx="2"/><rect x="60" y="141" width="48" height="12" rx="2"/><rect x="161" y="141" width="48" height="12" rx="2"/><rect x="262" y="141" width="48" height="12" rx="2"/></g>
    <g fill="#d6d6d6"><rect x="161" y="105" width="48" height="12" rx="2"/><rect x="212" y="105" width="48" height="12" rx="2"/><rect x="262" y="105" width="48" height="12" rx="2"/><rect x="60" y="178" width="48" height="12" rx="2"/><rect x="161" y="178" width="99" height="12" rx="2"/><rect x="262" y="178" width="48" height="12" rx="2"/><rect x="312" y="178" width="50" height="12" rx="2"/></g>
    <g font-size="4.5" text-anchor="middle" fill="#fff"><text x="84" y="77">Lorem ipsum</text><text x="134" y="77">Lorem ipsum</text><text x="211" y="77">Lorem ipsum</text><text x="337" y="77">Lorem ipsum</text><text x="84" y="149">Lorem ipsum</text><text x="185" y="149">Lorem ipsum</text><text x="286" y="149">Lorem ipsum</text></g>
    <g font-size="4.5" text-anchor="middle" fill="#888"><text x="185" y="113">Lorem ipsum</text><text x="236" y="113">Lorem ipsum</text><text x="286" y="113">Lorem ipsum</text><text x="84" y="186">Lorem ipsum</text><text x="210" y="186">Lorem ipsum</text><text x="286" y="186">Lorem ipsum</text><text x="337" y="186">Lorem ipsum</text></g>
  </svg>
  <span class="date">05/14/2024</span><span class="page">18</span>
</section>

<section class="slide" style="left:496.1px;top:597.6px">
  <h2 class="title">Roadmap II</h2><i class="rule"></i><div class="tab">PX</div>
  <svg class="chart" viewBox="0 0 380 219">
    <rect x="22" y="58" width="340" height="13" fill="#000"/>
    <g fill="#fff" font-size="4.2"><text x="25" y="67">Initiative</text><text x="80" y="67">Objective</text><text x="183" y="67">Jan</text><text x="198" y="67">Feb</text><text x="213" y="67">Mar</text><text x="228" y="67">Apr</text><text x="243" y="67">May</text><text x="258" y="67">Jun</text><text x="274" y="67">Jul</text><text x="289" y="67">Aug</text><text x="304" y="67">Sep</text><text x="319" y="67">Oct</text><text x="334" y="67">Nov</text><text x="349" y="67">Dec</text></g>
    <g fill="#bfbfbf"><rect x="180" y="71" width="30" height="24"/><rect x="195" y="95" width="15" height="24"/><rect x="210" y="119" width="45" height="24"/><rect x="255" y="143" width="46" height="24"/><rect x="301" y="167" width="15" height="23"/></g>
    <g fill="none" stroke="#000" stroke-width=".5"><rect x="22" y="71" width="340" height="119"/><path d="M22 95h340M22 119h340M22 143h340M22 167h340M77 71v119M180 71v119M195 71v119M210 71v119M225 71v119M240 71v119M255 71v119M271 71v119M286 71v119M301 71v119M316 71v119M331 71v119M346 71v119"/></g>
    <g fill="#333" font-size="4">
      <text x="25" y="85">Lorem ipsum</text><text x="25" y="109">Lorem ipsum</text><text x="25" y="133">Lorem ipsum</text><text x="25" y="157">Lorem ipsum</text><text x="25" y="181">Lorem ipsum</text>
      <text x="80" y="79">Short aim for this task,</text><text x="80" y="84">set over a couple of lines</text><text x="80" y="89">to fill the cell</text>
      <text x="80" y="103">Short aim for this task,</text><text x="80" y="108">set over a couple of lines</text><text x="80" y="113">to fill the cell</text>
      <text x="80" y="127">Short aim for this task,</text><text x="80" y="132">set over a couple of lines</text><text x="80" y="137">to fill the cell</text>
      <text x="80" y="151">Short aim for this task,</text><text x="80" y="156">set over a couple of lines</text><text x="80" y="161">to fill the cell</text>
      <text x="80" y="175">Short aim for this task,</text><text x="80" y="180">set over a couple of lines</text><text x="80" y="185">to fill the cell</text>
    </g>
  </svg>
  <span class="date">05/14/2024</span><span class="page">19</span>
</section>

<section class="slide" style="left:724.3px;top:597.6px">
  <div class="photo warm" role="img" aria-label="Technician in hard hat and safety vest calibrating equipment" style="left:0;top:0;width:144px;height:219px"></div>
  <div class="black-card" style="left:120px;top:63px;width:240px;height:101px"></div>
  <div style="left:167px;top:78px;font-size:15px;font-weight:700;color:var(--green)">02</div>
  <h2 style="left:166px;top:101px;font-size:23px;font-weight:700;line-height:25px;color:var(--white)">Name of<br>the section</h2>
</section>

<!-- Row 6 -->
<section class="slide" style="left:38.5px;top:737.1px">
  <i class="rule" style="left:0"></i><div class="tab">PX</div>
  <div class="photo warm" role="img" aria-label="Engineer in a safety vest working at a laptop" style="left:24px;top:42px;width:84px;height:164px"></div>
  <div class="photo" role="img" aria-label="Engineer working at a desk with tools" style="left:111px;top:42px;width:98px;height:88px;background:linear-gradient(135deg,#c8ccd0,#4d6a8a 55%,#2a2e33)"></div>
  <div class="photo warm" role="img" aria-label="Worker in a yellow vest holding a hard hat" style="left:111px;top:132px;width:98px;height:74px"></div>
  <span class="page">21</span>
</section>

<section class="slide" style="left:266.7px;top:737.1px">
  <h2 class="title">Slide Title</h2><i class="rule"></i><div class="tab">PX</div>
  <div class="body" style="left:22px;top:58px;width:165px;font-size:8.5px"><ul><li>Short bullet of body text that runs over a few lines to fill this column well.</li><li>A second bullet with a little more detail, set over several lines.</li></ul></div>
  <div class="body" style="left:193px;top:58px;width:165px;font-size:8.5px"><ul><li>Short bullet of body text that runs over a few lines to fill this column well.</li><li>A second bullet with a little more detail, set over several lines.</li></ul></div>
  <span class="date">05/14/2024</span><span class="page">22</span>
</section>

<section class="slide" style="left:496.1px;top:737.1px">
  <h2 class="title">Table of Comparisons</h2><i class="rule"></i><div class="tab">PX</div>
  <svg class="chart" viewBox="0 0 380 219">
    <g fill="#000"><rect x="95" y="53" width="65" height="14"/><rect x="163" y="53" width="65" height="14"/><rect x="230" y="53" width="65" height="14"/><rect x="298" y="53" width="65" height="14"/></g>
    <g fill="#fff" font-size="4.5" font-weight="700" text-anchor="middle"><text x="127" y="62">Lorem ipsum dolor</text><text x="195" y="62">Lorem ipsum dolor</text><text x="262" y="62">Lorem ipsum dolor</text><text x="330" y="62">Lorem ipsum dolor</text></g>
    <g fill="#efefef"><rect x="12" y="76" width="356" height="24"/><rect x="12" y="103" width="356" height="24"/><rect x="12" y="130" width="356" height="24"/><rect x="12" y="157" width="356" height="24"/></g>
    <g fill="#000"><circle cx="22" cy="88" r="7"/><circle cx="22" cy="115" r="7"/><circle cx="22" cy="142" r="7"/><circle cx="22" cy="169" r="7"/></g>
    <g fill="none" stroke="#fff" stroke-width=".8"><circle cx="22" cy="88" r="3"/><rect x="19" y="112" width="6" height="6"/><path d="M19 145v-4m3 4v-6m3 6v-3"/><rect x="19" y="166" width="6" height="6" rx="1"/></g>
    <g fill="#1f3550" font-size="5.5" font-weight="700"><text x="34" y="90">Lorem Ipsum</text><text x="34" y="117">Lorem Ipsum</text><text x="34" y="144">Lorem Ipsum</text><text x="34" y="171">Lorem Ipsum</text></g>
  </svg>
  <span class="date">05/14/2024</span><span class="page">23</span>
</section>

<section class="slide" style="left:724.3px;top:737.1px">
  <h2 class="title">Revenue</h2><i class="rule"></i><div class="tab">PX</div>
  <svg class="chart" viewBox="0 0 380 219">
    <g fill="#cfff00"><rect x="97" y="52" width="50" height="14"/><rect x="149" y="52" width="50" height="14"/><rect x="201" y="52" width="50" height="14"/><rect x="253" y="52" width="50" height="14"/><rect x="305" y="52" width="52" height="14"/></g>
    <g font-size="5" text-anchor="middle"><text x="122" y="62">Q1</text><text x="174" y="62">Q2</text><text x="226" y="62">Q3</text><text x="278" y="62">Q4</text><text x="331" y="62">Total</text></g>
    <rect x="24" y="68" width="71" height="119" fill="#000"/>
    <g fill="#efefef"><rect x="97" y="68" width="260" height="15"/><rect x="97" y="102" width="260" height="15"/><rect x="97" y="136" width="260" height="15"/><rect x="97" y="170" width="260" height="15"/></g>
    <g stroke="#fff" stroke-width=".6"><path d="M24 85h71M24 102h71M24 119h71M24 136h71M24 153h71M24 170h71"/></g>
    <g fill="#fff" font-size="6" font-weight="700"><text x="27" y="79">Product sales</text><text x="27" y="96">Labor</text><text x="27" y="113">Salaries</text><text x="27" y="130">Marketing</text><text x="27" y="147">Net income</text><text x="27" y="164">Rent</text><text x="27" y="181">Utilities</text></g>
    <g font-size="5" text-anchor="middle" fill="#222">
      <text x="122" y="78">$50,000</text><text x="174" y="78">$60,000</text><text x="226" y="78">$75,000</text><text x="278" y="78">$90,000</text><text x="331" y="78">$275,000</text>
      <text x="122" y="95">$20,000</text><text x="174" y="95">$24,000</text><text x="226" y="95">$30,000</text><text x="278" y="95">$36,000</text><text x="331" y="95">$110,000</text>
      <text x="122" y="112">$15,000</text><text x="174" y="112">$18,000</text><text x="226" y="112">$20,000</text><text x="278" y="112">$24,000</text><text x="331" y="112">$77,000</text>
      <text x="122" y="129">$7,000</text><text x="174" y="129">$8,000</text><text x="226" y="129">$9,000</text><text x="278" y="129">$10,000</text><text x="331" y="129">$34,000</text>
      <text x="122" y="146">$24,500</text><text x="174" y="146">$26,750</text><text x="226" y="146">$28,000</text><text x="278" y="146">$34,250</text><text x="331" y="146">$113,500</text>
      <text x="122" y="163">$5,000</text><text x="174" y="163">$5,000</text><text x="226" y="163">$5,000</text><text x="278" y="163">$5,000</text><text x="331" y="163">$20,000</text>
      <text x="122" y="180">$1,500</text><text x="174" y="180">$1,750</text><text x="226" y="180">$2,000</text><text x="278" y="180">$2,250</text><text x="331" y="180">$7,500</text>
    </g>
  </svg>
  <span class="date">05/14/2024</span><span class="page">24</span>
</section>

<!-- Row 7 -->
<section class="slide" style="left:37.9px;top:874.9px;background:var(--green)">
  <div style="left:0;top:78px;width:380px;text-align:center;font-size:36px;font-weight:800;line-height:40px">$500,000</div>
  <div style="left:0;top:121px;width:380px;text-align:center;font-size:9px">Big Numbers Get Attention</div>
</section>

<section class="slide" style="left:266.1px;top:874.9px">
  <h2 class="title">Graph Showing</h2><i class="rule"></i><div class="tab">PX</div>
  <svg class="chart" viewBox="0 0 380 219">
    <g stroke="#e4e4e4" stroke-width=".5"><path d="M75 80h215M75 92h215M75 104h215M75 116h215M75 128h215M75 140h215M75 152h215M75 164h215"/></g>
    <g fill="#888" font-size="3.5" text-anchor="end"><text x="72" y="82">700</text><text x="72" y="94">600</text><text x="72" y="106">500</text><text x="72" y="118">400</text><text x="72" y="130">300</text><text x="72" y="142">200</text><text x="72" y="154">100</text><text x="72" y="166">0</text></g>
    <rect x="97" y="130" width="11" height="34" fill="#cfff00"/><rect x="111" y="116" width="11" height="48" fill="#bfbfbf"/><rect x="125" y="98" width="11" height="66" fill="#000"/>
    <rect x="164" y="107" width="11" height="57" fill="#cfff00"/><rect x="178" y="92" width="11" height="72" fill="#bfbfbf"/><rect x="192" y="122" width="11" height="42" fill="#000"/>
    <rect x="231" y="104" width="11" height="60" fill="#cfff00"/><rect x="245" y="140" width="11" height="24" fill="#bfbfbf"/><rect x="259" y="110" width="11" height="54" fill="#000"/>
    <g font-size="3.5" fill="#555"><rect x="150" y="177" width="3" height="3" fill="#cfff00"/><text x="154" y="180">Series 1</text><rect x="170" y="177" width="3" height="3" fill="#bfbfbf"/><text x="174" y="180">Series 2</text><rect x="190" y="177" width="3" height="3" fill="#000"/><text x="194" y="180">Series 3</text></g>
  </svg>
  <span class="date">05/14/2024</span><span class="page">26</span>
</section>

<section class="slide" style="left:495px;top:874.9px">
  <h2 class="title">Sales for 2024</h2><i class="rule"></i><div class="tab">PX</div>
  <svg class="chart" viewBox="0 0 380 219">
    <g font-size="8"><rect x="29" y="60" width="4" height="4"/><text x="38" y="65">Q1</text><rect x="29" y="94" width="4" height="4" fill="#cfff00"/><text x="38" y="99">Q2</text><rect x="29" y="128" width="4" height="4" fill="#bfbfbf"/><text x="38" y="133">Q3</text><rect x="29" y="162" width="4" height="4" fill="#7f7f7f"/><text x="38" y="167">Q4</text></g>
    <g font-size="6" font-weight="700"><text x="38" y="76">$1,000,000,000</text><text x="38" y="114">$1,500,000,000</text><text x="38" y="146">$998,300,000</text><text x="38" y="180">$1,000,000,000</text></g>
    <g stroke="#ccc" stroke-width=".5"><path d="M38 82h60M38 120h60M38 152h60"/></g>
    <path d="M238 116L238 58A58 58 0 1 1 204.7 163.5Z" fill="#000"/>
    <path d="M238 116L204.7 163.5A58 58 0 0 1 183.5 96.2Z" fill="#cfff00"/>
    <path d="M238 116L183.5 96.2A58 58 0 0 1 209 65.8Z" fill="#bfbfbf"/>
    <path d="M238 116L209 65.8A58 58 0 0 1 238 58Z" fill="#7f7f7f"/>
    <g font-size="4.5" fill="#555"><rect x="302" y="113" width="3" height="3"/><text x="307" y="116">1st Qtr</text><rect x="302" y="125" width="3" height="3" fill="#cfff00"/><text x="307" y="128">2nd Qtr</text><rect x="302" y="137" width="3" height="3" fill="#bfbfbf"/><text x="307" y="140">3rd Qtr</text><rect x="302" y="149" width="3" height="3" fill="#7f7f7f"/><text x="307" y="152">4th Qtr</text></g>
  </svg>
  <span class="date">05/14/2024</span><span class="page">27</span>
</section>

<section class="slide" style="left:724.9px;top:874.9px">
  <h2 class="title">Testimonials</h2><i class="rule"></i><div class="tab">PX</div>
  <svg class="chart" viewBox="0 0 380 219">
    <circle cx="137" cy="20" r="4" fill="#000"/>
    <rect x="43" y="65" width="125" height="40" rx="4" fill="#cfff00"/><path d="M86 104l8 10 8-10z" fill="#cfff00"/>
    <rect x="178" y="65" width="126" height="40" rx="4" fill="#000"/><path d="M233 104l8 9 8-9z" fill="#000"/>
    <rect x="77" y="124" width="126" height="40" rx="4" fill="#000"/><path d="M122 163l8 10 8-10z" fill="#000"/>
    <rect x="219" y="124" width="126" height="40" rx="4" fill="#cfff00"/><path d="M267 163l8 9 8-9z" fill="#cfff00"/>
  </svg>
  <span class="date">05/14/2024</span><span class="page">28</span>
</section>

<!-- Row 8 -->
<section class="slide" style="left:37.9px;top:1016.1px">
  <div class="black-card" style="left:8px;top:15px;width:131px;height:185px"></div>
  <div style="left:139px;top:15px;width:233px;height:98px;background:var(--green)"></div>
  <svg class="chart" viewBox="0 0 380 219">
    <g fill="none" stroke="#fff" stroke-width="5"><path d="M53 115a22 22 0 0 1 44 0"/><path d="M92 128q0 12-14 12"/></g>
    <rect x="46" y="110" width="11" height="20" rx="4" fill="#fff"/><rect x="93" y="110" width="11" height="20" rx="4" fill="#fff"/>
    <circle cx="75" cy="119" r="13" fill="#fff"/><rect x="73" y="117" width="4" height="9" fill="#000"/><circle cx="75" cy="112" r="2.2" fill="#000"/>
    <path d="M165 133l8-4-4 8-1-3z" fill="#000"/>
    <path d="M165 176q1 4 5 5l2-2-2-2-1 1q-2-1-2-2l1-1-2-2z" fill="#000"/>
    <rect x="165" y="184" width="6" height="4" fill="#000"/>
    <g fill="#000"><circle cx="338" cy="185" r="4.5"/><circle cx="349" cy="185" r="4.5"/><circle cx="360" cy="185" r="4.5"/></g>
  </svg>
  <div style="left:165px;top:88px;font-size:20px;font-weight:700">Contact</div>
  <div style="left:178px;top:129px;font-size:6px;font-weight:600;line-height:1.25">Lorem ipsum dolor sit amet,<br>consectetur adipiscing elit</div>
  <div style="left:178px;top:174px;font-size:6px;font-weight:600;line-height:1.35">555 014 2368<br>hello@pellionlabs.com</div>
</section>

<section class="slide" style="left:264.6px;top:1016.1px;background:var(--black)">
  <div style="left:0;top:0;width:380px;height:1px;background:#222"></div>
  <div style="left:0;top:136px;width:380px;height:1px;background:#555"></div>
  <div style="left:30px;top:119px;padding:0 6px;background:var(--black);color:var(--white);font-size:26px;font-weight:700;line-height:32px">Thank You</div>
  <div style="left:203px;top:135px;width:12px;height:2px;background:var(--green)"></div>
  <div style="left:0;top:217px;width:380px;height:1px;background:#333"></div>
</section>

</main>
</body>
</html>
```